Label design for loose leaf tea pouches and tins

Starting my loose leaf tea business and looking for product labels.
I already have logo designed and would love it to be worked into the label;
Label sizes and sample text is in the attachments;
Pouches and tins pictures are also in the attachments.

looking for the recommendation on what is the best color for the pouch.
Updates

Here is the link: https://sheets.plorvane.example/grid/d/7kTq2mWx9LpZ4vRn8cYb3HsJf6DaE1uQ0oGtXiKe/edit

Adding the pdf since plorvane links do not work here

Target Market(s)

Women and men, 35+, USA

Font styles to use
Serif

Requirements
Must have
• Front and back label

```html
<!DOCTYPE html>
<html lang="en">
<head>
<meta charset="utf-8">
<title>Still Hour – Leafwell Tea Pouch Labels</title>
<link rel="stylesheet" href="https://fonts.googleapis.com/css2?family=Josefin+Sans:wght@300;400&family=Playfair+Display:ital@1&family=Cormorant+Garamond:wght@500;700&display=swap">
<style>
  :root {
    --plum: #5b2476;
    --plum-light: #6d3289;
    --navy: #1b1c36;
    --gold: #e7c48f;
    --gold-line: #c9a25f;
    --cream: #f7ecdc;
    --paper: #ffffff;
    --pattern-plum: #4e1e66;
    --pattern-navy: #2b2248;
  }
  * { box-sizing: border-box; margin: 0; padding: 0; }
  html, body { width: 1200px; height: 1200px; overflow: hidden; background: var(--paper); }
  .canvas { position: relative; width: 1200px; height: 1200px; }

  .pouch {
    position: absolute; top: 204px; width: 562px; height: 800px;
    border-radius: 4px; overflow: hidden;
    background: linear-gradient(to bottom, var(--plum) 0, var(--plum-light) 392px, var(--navy) 392px);
  }
  .pouch--front { left: 28px; }
  .pouch--back { left: 614px; }
  .pouch__band { position: absolute; left: 0; right: 0; top: 390px; height: 4px; background: var(--gold-line); }
  .pouch__pattern { position: absolute; }
  .pouch__pattern--top { left: 0; right: 0; top: 0; height: 90px; background: linear-gradient(to bottom, var(--pattern-plum), transparent); opacity: .7; }
  .pouch__pattern--bottom { right: 0; bottom: 0; width: 320px; height: 110px; background: linear-gradient(to top, var(--pattern-navy), transparent); opacity: .8; }

  .brand { position: absolute; left: 0; right: 0; text-align: center; font-family: "Cormorant Garamond", serif; font-weight: 700; color: var(--gold); letter-spacing: .16em; }
  .brand__dot { display: block; margin: 0 auto 16px; width: 64px; height: 64px; border-radius: 50%; background: var(--gold); }
  .brand--front { top: 140px; font-size: 34px; }

  .title-box { position: absolute; border: 1.5px solid var(--gold-line); border-radius: 14px; text-align: center; }
  .title-box__tag { position: absolute; top: -12px; left: 50%; transform: translateX(-50%); padding: 0 12px; font-family: "Cormorant Garamond", serif; font-weight: 500; font-size: 15px; color: var(--cream); white-space: nowrap; }
  .title-box__tag::before, .title-box__tag::after { content: ""; display: inline-block; width: 8px; height: 8px; border-radius: 50%; border: 1.5px solid var(--gold); vertical-align: middle; margin: 0 8px; }
  .title-box__name { font-family: "Josefin Sans", sans-serif; font-weight: 300; color: #ffffff; line-height: .88; }

  .pouch--front .title-box { left: 120px; top: 290px; width: 330px; height: 200px; }
  .pouch--front .title-box__tag { background: var(--plum-light); }
  .pouch--front .title-box__name { font-size: 94px; padding-top: 26px; }

  .pouch--back .title-box { left: 116px; top: 62px; width: 338px; height: 204px; }
  .pouch--back .title-box__tag { background: var(--plum); }
  .pouch--back .title-box__name { font-size: 94px; padding-top: 26px; }
  .brand--back { position: absolute; bottom: -12px; left: 50%; transform: translateX(-50%); padding: 0 12px; background: var(--plum-light); font-family: "Cormorant Garamond", serif; font-weight: 700; font-size: 16px; letter-spacing: .14em; color: var(--gold); white-space: nowrap; }
  .brand--back::before { content: ""; display: inline-block; width: 18px; height: 18px; border-radius: 50%; background: var(--gold); vertical-align: middle; margin-right: 10px; }

  .tagline { position: absolute; left: 0; right: 0; text-align: center; font-family: "Playfair Display", serif; font-style: italic; color: #cbb8d6; font-size: 20px; line-height: 1.22; }
  .pouch--front .tagline { top: 572px; color: #b8b3c8; }
  .pouch--back .tagline { top: 300px; }

  .net { position: absolute; left: 74px; top: 716px; font-family: "Cormorant Garamond", serif; color: var(--cream); }
  .net__weight { font-weight: 700; font-size: 17px; letter-spacing: .04em; }
  .net__type { font-weight: 500; font-size: 16px; margin-top: 6px; }

  .info { position: absolute; font-family: "Cormorant Garamond", serif; color: var(--cream); }
  .info__head { font-weight: 700; font-size: 15px; color: var(--gold); padding-bottom: 12px; border-bottom: 1px dotted #5d5a78; margin-bottom: 10px; }
  .info--benefits { left: 118px; top: 442px; width: 210px; padding-right: 14px; border-right: 1px dotted #5d5a78; }
  .info--benefits p { font-weight: 500; font-size: 14.2px; line-height: 1.27; }
  .info--ingredients { left: 342px; top: 446px; width: 120px; }
  .info--ingredients ul { list-style: none; font-weight: 500; font-size: 14.2px; line-height: 1.27; }
  .facts { position: absolute; left: 122px; top: 680px; font-family: "Cormorant Garamond", serif; font-weight: 700; font-size: 14.5px; line-height: 1.4; color: var(--cream); padding-bottom: 10px; border-bottom: 1px dotted #5d5a78; }
</style>
</head>
<body>
<main class="canvas">

  <section class="pouch pouch--front" aria-label="Front label">
    <div class="pouch__pattern pouch__pattern--top" role="img" aria-label="Faint botanical sprig pattern"></div>
    <div class="pouch__band"></div>
    <div class="pouch__pattern pouch__pattern--bottom" role="img" aria-label="Faint wildflower silhouettes"></div>

    <div class="brand brand--front"><span class="brand__dot"></span>LEAFWELL</div>

    <div class="title-box">
      <span class="title-box__tag">Premium Blend</span>
      <div class="title-box__name">Still<br>Hour</div>
    </div>

    <p class="tagline">Delicious concoction of<br>Indian herbs and flowers<br>to help you settle<br>and unwind</p>

    <div class="net">
      <div class="net__weight">3.4 OZ / 100g</div>
      <div class="net__type">Decaffinated Loose Leaf Tea</div>
    </div>
  </section>

  <section class="pouch pouch--back" aria-label="Back label">
    <div class="pouch__pattern pouch__pattern--top" role="img" aria-label="Faint botanical sprig pattern"></div>
    <div class="pouch__band"></div>
    <div class="pouch__pattern pouch__pattern--bottom" role="img" aria-label="Faint wildflower silhouettes"></div>

    <div class="title-box">
      <span class="title-box__tag">Premium Blend</span>
      <div class="title-box__name">Still<br>Hour</div>
      <span class="brand--back">LEAFWELL</span>
    </div>

    <p class="tagline">Delicious concoction of Indian<br>herbs and flowers to help you<br>settle and unwind</p>

    <div class="info info--benefits">
      <h3 class="info__head">BENEFITS</h3>
      <p>Truly magic wellness potion formulated with combination of world-class ingridients. Still Hour tea calms you down, warms you up, eases anxiety and fights signs of depression. Turmeric, cardamom and ginger reduce symptoms of gas and bloating and facilitate digestion.</p>
    </div>

    <div class="info info--ingredients">
      <h3 class="info__head">INGRIDIENTS</h3>
      <ul>
        <li>Chamomile</li><li>Mary Gold</li><li>Rooibos</li><li>Liquorice Root</li><li>Apple</li>
        <li>Lemon Peels</li><li>Cloves</li><li>Black Cardamom</li><li>Turmeric</li><li>Ginger</li>
      </ul>
    </div>

    <div class="facts">
      Country of origin: India<br>
      3.4 OZ / 100g, 50 servings<br>
      Decaffinated.
    </div>
  </section>

</main>
</body>
</html>
```